Larchfield Shopping Centre main sign re-design project

We would like to refresh the look of the main sign we have on the corner of a block of shops to make it more contemproary and vibrant.

A picture of the existing sign which reads Larchfield Shopping Centre can be found in attached PDF and at the following URL.

http://www.quentorprop.example.nz/~/media/Listings/Region%20One/Sample%20Town/Sample%20Town%20CBD/418207/Images/418207_1.ashx?bc=Gainsboro&as=1&h=550&w=980&ma=1

Larchfield Shopping Centre is also know locally as Larchfield Plaza, but the key word is Larchfield.

The existing signage has a flower/clover pattern on it which I think was just added to create a bit of interest. The building is located in a town surrounded by farm land.

I do quite like the organic feel of plant leaves or certain flowers - preferably New Zealand native plants for instance - the Kowhai flower or leaf block, pohutukawa, or kaka beak - reference images can be found with google image search

Geometric patterns could also be an option.

Once again the imagery is only to soften the sign and add some interest.
Updates

                                        Additional images of existing signage added

Project Deadline Extended
Reason: Closing date extended to allow for fact that lead up to Christmas is a busy time of year for many people.

Target Market(s)

The target audience is premium shopper

Industry/Entity Type

Building

Requirements
Must have
• Must have the words: Larchfield Shopping Centre.
The big M is not essential, and I would rather the emphasis was on the word Larchfield.
Should not have
• Should not be brown. We want the sign to feel more contemporary, but not too hard. The current pale brown feels too soft in comparison with the look of the building.

```html
<!DOCTYPE html>
<html lang="en">
<head>
<meta charset="utf-8">
<title>Larchfield Shopping Centre – Main Sign</title>
<link rel="stylesheet" href="https://fonts.googleapis.com/css2?family=Oswald:wght@600;700&display=swap">
<style>
  :root {
    --backdrop: #f2f2f2;
    --sign-red-top: #e8132f;
    --sign-red-base: #cc0f31;
    --sign-white: #ffffff;
    --text-black: #111111;
    --text-white: #ffffff;
    --art-red: #e23a4c;
    --art-orange: #f39a4a;
  }
  html, body {
    margin: 0;
    padding: 0;
    overflow: hidden;
  }
  body {
    width: 1200px;
    height: 744px;
    background: var(--backdrop);
    position: relative;
  }
  .sign {
    position: absolute;
    left: 431px;
    top: 27px;
    width: 337px;
    height: 686px;
    display: flex;
    flex-direction: column;
    box-shadow: 6px 8px 10px rgba(0, 0, 0, 0.35);
  }
  .sign__cap {
    height: 92px;
    background: var(--sign-red-top);
  }
  .sign__panel {
    height: 426px;
    background: var(--sign-white);
    position: relative;
  }
  .sign__artwork {
    position: absolute;
    left: 14px;
    top: 74px;
    width: 309px;
    height: 164px;
    background: linear-gradient(180deg, var(--art-orange) 0%, var(--art-red) 100%);
    opacity: 0.85;
  }
  .sign__name {
    position: absolute;
    left: 0;
    right: 0;
    top: 256px;
    margin: 0;
    text-align: center;
    font-family: "Oswald", sans-serif;
    font-weight: 700;
    font-size: 58px;
    line-height: 1.1;
    letter-spacing: 0.04em;
    color: var(--text-black);
  }
  .sign__base {
    flex: 1;
    background: var(--sign-red-base);
    display: flex;
    flex-direction: column;
    align-items: center;
    justify-content: center;
    font-family: "Oswald", sans-serif;
    font-weight: 600;
    font-size: 52px;
    line-height: 1.12;
    letter-spacing: 0.1em;
    color: var(--text-white);
    padding-left: 0.1em;
  }
</style>
</head>
<body>
  <div class="sign">
    <div class="sign__cap"></div>
    <div class="sign__panel">
      <div class="sign__artwork" role="img" aria-label="Illustration area: fan of red kaka beak flower petals with orange tips on a green stem"></div>
      <h1 class="sign__name">LARCHFIELD</h1>
    </div>
    <div class="sign__base">
      <span>SHOPPING</span>
      <span>CENTRE</span>
    </div>
  </div>
</body>
</html>
```